Business Card Design using new attached logo

We are a family run Plumbing and Heating firm looking to improve our company image with an improved business card and new logo.We are looking to keep the company colour (Blue) involved in our design

Reason: New logo added which needs to be incorporated on designs

Industry/Entity Type

Business

Contact Information for Business Card

See attachment of all info required.

Requirements
Must have
• We have just picked a new company logo which is attached.
• Could you please provide your business card designs using this logo.
• We are looking for the logo on the back as well as the front with all the info required

```html
<!DOCTYPE html>
<html lang="en">
<head>
<meta charset="utf-8">
<title>Kelver Services – Business Card</title>
<link rel="stylesheet" href="https://fonts.googleapis.com/css2?family=Roboto:wght@300;400;500;700&display=swap">
<style>
  :root {
    --page-bg: #e9eaee;
    --card-navy: #0e1f5e;
    --card-navy-deep: #0a1848;
    --band-blue: #2b8cf7;
    --brand-blue: #1b36a6;
    --ink: #1c1c22;
    --ink-soft: #3a3a44;
    --paper: #ffffff;
    --rule: #23378f;
  }
  * { box-sizing: border-box; margin: 0; padding: 0; }
  html, body {
    width: 1200px;
    height: 900px;
    overflow: hidden;
    background: var(--page-bg);
    font-family: "Roboto", Arial, sans-serif;
  }
  .canvas {
    position: relative;
    width: 1200px;
    height: 900px;
  }
  .card {
    position: absolute;
    top: 281px;
    width: 582px;
    height: 337px;
    overflow: hidden;
    box-shadow: 0 6px 18px rgba(0, 0, 0, 0.18);
  }
  .card--front {
    left: 10px;
    background: radial-gradient(ellipse at 50% 45%, var(--card-navy) 0%, var(--card-navy-deep) 100%);
  }
  .card--back {
    left: 607px;
    background: var(--paper);
  }
  .brand-name {
    position: absolute;
    font-weight: 500;
    font-size: 34px;
    letter-spacing: 3px;
    line-height: 1.05;
    text-align: center;
    text-transform: uppercase;
  }
  .card--front .brand-name {
    left: 0;
    width: 582px;
    top: 132px;
    color: var(--paper);
  }
  .card--back .brand-name {
    left: 18px;
    width: 250px;
    top: 130px;
    font-size: 30px;
    color: var(--brand-blue);
  }
  .name-band {
    position: absolute;
    background: var(--band-blue);
    text-align: center;
    color: var(--ink);
    padding-top: 4px;
  }
  .card--front .name-band {
    left: 292px;
    top: 285px;
    width: 290px;
    height: 52px;
  }
  .card--back .name-band {
    left: 291px;
    top: 2px;
    width: 291px;
    height: 52px;
  }
  .name-band__name {
    font-weight: 700;
    font-size: 19px;
    letter-spacing: 0.2px;
    line-height: 24px;
  }
  .name-band__title {
    font-weight: 400;
    font-size: 15px;
    line-height: 18px;
  }
  .divider {
    position: absolute;
    left: 286px;
    top: 92px;
    width: 2px;
    height: 158px;
    background: var(--rule);
  }
  .contact {
    position: absolute;
    left: 330px;
    top: 120px;
    list-style: none;
    font-weight: 300;
    font-size: 15px;
    color: var(--ink-soft);
    line-height: 19px;
  }
  .contact__item {
    position: relative;
    padding-left: 38px;
  }
  .contact__item--address { margin-bottom: 13px; }
  .contact__item--fax { margin-bottom: 15px; }
  .contact__icon {
    position: absolute;
    left: 0;
    top: 1px;
    width: 22px;
    height: 18px;
  }
</style>
</head>
<body>
  <main class="canvas">
    <section class="card card--front" aria-label="Business card front">
      <div class="brand-name">Kelver Services</div>
      <div class="name-band">
        <div class="name-band__name">DANIEL MARSH</div>
        <div class="name-band__title">Director</div>
      </div>
    </section>

    <section class="card card--back" aria-label="Business card back">
      <div class="name-band">
        <div class="name-band__name">DANIEL MARSH</div>
        <div class="name-band__title">Director</div>
      </div>
      <div class="brand-name">Kelver Services</div>
      <div class="divider"></div>
      <ul class="contact">
        <li class="contact__item contact__item--address">4820-117 Avenue Edmonton,<br>AB T5W 0K2 780-555-0142</li>
        <li class="contact__item contact__item--fax">
          <svg class="contact__icon" viewBox="0 0 22 18" aria-hidden="true">
            <path d="M2 6 Q11 0 20 6 L18 8 L15 7 L15 5 Q11 3.5 7 5 L7 7 L4 8 Z" fill="#2a3f86"/>
            <path d="M5 9 L17 9 L19 17 L3 17 Z" fill="#2a3f86"/>
            <circle cx="11" cy="13" r="2.2" fill="#ffffff"/>
          </svg>
          Fax 780-555-0187
        </li>
        <li class="contact__item">
          <svg class="contact__icon" viewBox="0 0 22 18" aria-hidden="true">
            <rect x="2" y="3" width="18" height="13" fill="none" stroke="#2a3f86" stroke-width="1.5"/>
            <path d="M2 3 L11 10 L20 3 M2 16 L8.5 8.5 M20 16 L13.5 8.5" fill="none" stroke="#2a3f86" stroke-width="1.5"/>
          </svg>
          office@kelverservices.com
        </li>
      </ul>
    </section>
  </main>
</body>
</html>
```